TLW Business Card Design

Services for small businesses: Bookkeeping
BAS
Payroll
Software advice and sales
Can provide training for staff
Programs used: ZEPT, Talvin, Quil
Clients software or mine.
Inhouse or external (pickup paperwork, process and return)
I provide individual solutions based on the clients business
I am a sole trader
Industry/Entity Type
Training
Contact Information for Business Card
TLW Bookkeeping Solutions
Marlena Voughton, Qualified Bookkeeping Consultant
Registered BAS Agent
PO Box 736, Elmvale SA 5127
P: 0491 385 617
F: 08 8579 6014
Logo Text
TLW Bookkeeping Solutions
Requirements
Must have
- I don't have a logo but anything financial would be great.
My name, title, business name, Registered BAS agent, contact details.
Nice to have
- The "nice to haves" are the types of services (ie: Payroll, Bookkeeping, etc) and the software to be used (ie: ZEPT, Talvin, Quil).

```html
<!DOCTYPE html>
<html lang="en">
<head>
<meta charset="utf-8">
<title>TLW Bookkeeping Solutions – Business Card</title>
<link rel="stylesheet" href="https://fonts.googleapis.com/css2?family=Jost:wght@400;500;700;800&display=swap">
<style>
  :root {
    --page: #d9d4cd;
    --card: #0e0e0e;
    --ghost: #1c1c1c;
    --ink: #ffffff;
    --muted: #d6d6d6;
    --accent: #f2e600;
  }
  * { box-sizing: border-box; margin: 0; padding: 0; }
  html, body { width: 1200px; height: 800px; overflow: hidden; }
  body {
    background: var(--page);
    font-family: "Jost", "Futura", sans-serif;
    color: var(--ink);
    position: relative;
  }
  .card {
    position: absolute;
    width: 560px;
    height: 320px;
    background: var(--card);
    overflow: hidden;
    box-shadow: 0 6px 18px rgba(0,0,0,0.25);
  }
  .card--front { left: 110px; top: 50px; }
  .card--back { left: 530px; top: 430px; }

  .ghost-mark {
    position: absolute;
    left: 0;
    top: -10px;
    font-weight: 800;
    font-size: 290px;
    line-height: 1;
    letter-spacing: -8px;
    color: var(--ghost);
    white-space: nowrap;
    user-select: none;
  }
  .divider {
    position: absolute;
    width: 4px;
  }

  /* Front */
  .brand {
    position: absolute;
    left: 30px;
    top: 118px;
    width: 250px;
    font-weight: 700;
    color: var(--ink);
  }
  .brand__name { font-size: 46px; line-height: 1; letter-spacing: 2px; }
  .brand__sub { font-size: 21px; line-height: 1.15; margin-top: 4px; }
  .credentials {
    position: absolute;
    left: 20px;
    top: 246px;
    width: 280px;
    text-align: center;
    font-size: 11.5px;
    line-height: 1.35;
    color: var(--ink);
  }
  .card--front .divider { left: 298px; top: 26px; height: 170px; }
  .contact {
    position: absolute;
    left: 322px;
    top: 22px;
    width: 230px;
  }
  .contact__name { font-size: 20px; font-weight: 700; line-height: 1.1; }
  .contact__title { font-size: 10.5px; color: var(--muted); margin-top: 2px; }
  .contact__address {
    font-size: 14px;
    line-height: 1.3;
    margin: 26px 0 0 24px;
    color: var(--muted);
  }
  .contact__list { list-style: none; margin: 26px 0 0 24px; }
  .contact__item {
    display: flex;
    align-items: center;
    gap: 6px;
    font-size: 14px;
    line-height: 1.45;
    color: var(--muted);
  }
  .contact__item svg { width: 14px; height: 14px; flex: none; }

  /* Back */
  .card--back .divider { left: 292px; top: 92px; height: 150px; }
  .services, .software { position: absolute; list-style: none; }
  .services { left: 96px; top: 134px; }
  .software { left: 312px; top: 78px; }
  .services li, .software li {
    display: flex;
    align-items: center;
    gap: 10px;
    font-size: 23px;
    font-weight: 500;
    line-height: 1.2;
  }
  .services li:nth-child(2) { margin-left: 10px; }
  .services li:nth-child(3) { margin-left: 20px; }
  .services li:nth-child(4) { margin-left: 30px; }
  .software li:nth-child(2) { margin-left: 8px; }
  .software li:nth-child(3) { margin-left: 16px; }
  .software li:nth-child(4) { margin-left: 24px; }
  .bullet { width: 20px; height: 12px; flex: none; }
  .tagline {
    position: absolute;
    left: 190px;
    top: 258px;
    font-size: 23px;
    font-weight: 500;
  }
</style>
</head>
<body>

<section class="card card--front" aria-label="Business card front">
  <div class="ghost-mark" aria-hidden="true">TLW</div>

  <div class="brand">
    <div class="brand__name">TLW</div>
    <div class="brand__sub">Bookkeeping Solutions</div>
  </div>

  <p class="credentials">Registered BAS Agent 47293 118<br>Tailored solutions based on your business structure</p>

  <svg class="divider" viewBox="0 0 4 170" preserveAspectRatio="none" aria-hidden="true">
    <polygon points="1.5,0 2.5,0 4,170 0,170" fill="var(--accent)"/>
  </svg>

  <div class="contact">
    <h1 class="contact__name">Marlena Voughton</h1>
    <p class="contact__title">Qualified Bookkeeping Consultant</p>
    <p class="contact__address">PO Box 736,<br>Elmvale SA 5127</p>
    <ul class="contact__list">
      <li class="contact__item">
        <svg viewBox="0 0 16 16" aria-label="Mobile"><rect x="4.5" y="1" width="7" height="14" rx="1.5" fill="none" stroke="currentColor" stroke-width="1.4"/><circle cx="8" cy="12.5" r="0.9" fill="currentColor"/></svg>
        0491 385 617
      </li>
      <li class="contact__item">
        <svg viewBox="0 0 16 16" aria-label="Phone"><path d="M2 6 Q8 1 14 6 L12 8 L10 6.5 L6 6.5 L4 8 Z" fill="currentColor"/><rect x="3.5" y="8.5" width="9" height="6" rx="1" fill="none" stroke="currentColor" stroke-width="1.3"/></svg>
        08 8579 6014
      </li>
      <li class="contact__item">
        <svg viewBox="0 0 16 16" aria-label="Email"><rect x="1.5" y="3.5" width="13" height="9" fill="none" stroke="currentColor" stroke-width="1.3"/><polyline points="1.5,3.5 8,9 14.5,3.5" fill="none" stroke="currentColor" stroke-width="1.3"/></svg>
        tlwbooks@mailora.com
      </li>
    </ul>
  </div>
</section>

<section class="card card--back" aria-label="Business card back">
  <div class="ghost-mark" aria-hidden="true">TLW</div>

  <svg class="divider" viewBox="0 0 4 150" preserveAspectRatio="none" aria-hidden="true">
    <polygon points="1.5,0 2.5,0 4,150 0,150" fill="var(--accent)"/>
  </svg>

  <ul class="services">
    <li><svg class="bullet" viewBox="0 0 20 12" aria-hidden="true"><polygon points="0,4 12,4 12,0 20,6 12,12 12,8 0,8" fill="var(--accent)"/></svg>BAS</li>
    <li><svg class="bullet" viewBox="0 0 20 12" aria-hidden="true"><polygon points="0,4 12,4 12,0 20,6 12,12 12,8 0,8" fill="var(--accent)"/></svg>Payroll</li>
    <li><svg class="bullet" viewBox="0 0 20 12" aria-hidden="true"><polygon points="0,4 12,4 12,0 20,6 12,12 12,8 0,8" fill="var(--accent)"/></svg>Training</li>
    <li><svg class="bullet" viewBox="0 0 20 12" aria-hidden="true"><polygon points="0,4 12,4 12,0 20,6 12,12 12,8 0,8" fill="var(--accent)"/></svg>Bookkeeping</li>
  </ul>

  <ul class="software">
    <li><svg class="bullet" viewBox="0 0 20 12" aria-hidden="true"><polygon points="0,4 12,4 12,0 20,6 12,12 12,8 0,8" fill="var(--accent)"/></svg>Quil,</li>
    <li><svg class="bullet" viewBox="0 0 20 12" aria-hidden="true"><polygon points="0,4 12,4 12,0 20,6 12,12 12,8 0,8" fill="var(--accent)"/></svg>ZEPT,</li>
    <li><svg class="bullet" viewBox="0 0 20 12" aria-hidden="true"><polygon points="0,4 12,4 12,0 20,6 12,12 12,8 0,8" fill="var(--accent)"/></svg>Talvin,</li>
    <li><svg class="bullet" viewBox="0 0 20 12" aria-hidden="true"><polygon points="0,4 12,4 12,0 20,6 12,12 12,8 0,8" fill="var(--accent)"/></svg>Ledgerly Planner</li>
  </ul>

  <p class="tagline">Software advice and sales</p>
</section>

</body>
</html>
```